Software Company Business Card

We are looking for a new design of our business card. The design will also be used in the rest of our branding and marketing materials as we want to keep it all uniform. We sell POS software to fine/luxury jewelers and also offer other business services as well to help the jeweler manage their business and need something more updated, technical and fresh, preferably more on the masculine side. We do not want any designs with gems in them but if possible would like to incorporate the circle and arrow in the logo into the design, but not a requirement if you can't make it work. I would like to see a variety of the mix. The colors need to remain our blue and orange and the logo can not change. The squiggly lines have been used as our corporate identity for over 20 years and its time to update. Our company name is PELK (Bright Ledger Counter Solutions).

Target Market(s)

High End Jewelers

Industry/Entity Type

Software

Contact Information for Business Card

Requirements
Must have
• Our logo and the colors must remain the same. Blue is #d95d39 and Orange is #0f5682.
Nice to have
• The circle and arrow incorporated but not a requirement.
Should not have
• Anything jewelry or gem related.

```html
<!DOCTYPE html>
<html lang="en">
<head>
<meta charset="utf-8">
<title>PELK Business Card</title>
<link href="https://fonts.googleapis.com/css2?family=Montserrat:wght@400;500;700;800;900&display=swap" rel="stylesheet">
<style>
  :root {
    --brand-blue: #0f5682;
    --brand-orange: #d95d39;
    --card-white: #ffffff;
    --stage: #1f1f21;
    --text-light: #ffffff;
  }
  * { box-sizing: border-box; margin: 0; padding: 0; }
  html, body { width: 1200px; height: 1200px; overflow: hidden; }
  body {
    background: var(--stage);
    font-family: "Montserrat", sans-serif;
    position: relative;
  }
  .card {
    position: absolute;
    left: 180px;
    width: 840px;
    height: 480px;
    border-radius: 28px;
    overflow: hidden;
    background: var(--card-white);
    box-shadow: 0 18px 40px rgba(0,0,0,0.45);
  }
  .card-front { top: 90px; }
  .card-back { top: 630px; }

  /* Front */
  .front-logo {
    position: absolute;
    left: 50%; top: 50%;
    transform: translate(-50%, -50%);
    display: flex; flex-direction: column; align-items: flex-start;
  }
  .wordmark-row { display: flex; align-items: center; gap: 18px; }
  .wordmark {
    font-weight: 900;
    color: var(--brand-blue);
    font-size: 132px;
    line-height: 0.9;
    letter-spacing: -2px;
  }
  .mark-dot {
    width: 92px; height: 92px;
    border-radius: 50%;
    background: var(--brand-orange);
    align-self: flex-start;
  }
  .tagline {
    margin-top: 10px;
    font-weight: 800;
    font-size: 17px;
    letter-spacing: 0.5px;
    color: var(--brand-orange);
    text-transform: uppercase;
  }

  /* Back */
  .brand-strip {
    position: absolute; left: 0; top: 0;
    width: 260px; height: 100%;
    background: var(--card-white);
  }
  .strip-logo {
    position: absolute;
    left: 130px; top: 240px;
    transform: translate(-50%, -50%) rotate(-90deg);
    display: flex; flex-direction: column; align-items: flex-start;
  }
  .strip-logo .wordmark { font-size: 110px; }
  .strip-logo .mark-dot { width: 76px; height: 76px; }
  .strip-logo .tagline { font-size: 13px; margin-top: 8px; }

  .info-panel {
    position: absolute; left: 260px; top: 0;
    width: 580px; height: 100%;
    background: var(--brand-blue);
    color: var(--text-light);
    padding: 56px 0 0 70px;
  }
  .panel-notch {
    position: absolute; left: 260px; top: 112px;
    width: 0; height: 0;
    border-top: 14px solid transparent;
    border-bottom: 14px solid transparent;
    border-left: 18px solid var(--brand-orange);
  }
  .person-name {
    font-weight: 800; font-size: 30px;
    letter-spacing: 0.5px; text-transform: uppercase;
  }
  .person-title { font-weight: 400; font-size: 21px; margin-top: 4px; }
  .address {
    font-style: normal;
    font-size: 22px; line-height: 1.3;
    margin-top: 70px; margin-left: 70px;
  }
  .contact-list { list-style: none; margin-top: 12px; margin-left: 70px; }
  .contact-list li {
    display: flex; align-items: center; gap: 12px;
    font-size: 21px; line-height: 1.35;
  }
  .contact-icon { width: 20px; height: 20px; flex: none; }
</style>
</head>
<body>

<section class="card card-front" aria-label="Card front">
  <div class="front-logo">
    <div class="wordmark-row">
      <span class="wordmark">PELK</span>
      <span class="mark-dot" aria-hidden="true"></span>
    </div>
    <span class="tagline">Bright Ledger Counter Solutions</span>
  </div>
</section>

<section class="card card-back" aria-label="Card back">
  <div class="brand-strip">
    <div class="strip-logo">
      <div class="wordmark-row">
        <span class="wordmark">PELK</span>
        <span class="mark-dot" aria-hidden="true"></span>
      </div>
      <span class="tagline">Bright Ledger Counter Solutions</span>
    </div>
  </div>

  <div class="info-panel">
    <h1 class="person-name">Graham Whitcombe</h1>
    <p class="person-title">Director of Global Operations</p>

    <address class="address">
      1480 Meridian Park Drive<br>
      Suite 210<br>
      Carson Falls, NV 89510,<br>
      US
    </address>

    <ul class="contact-list">
      <li>
        <svg class="contact-icon" viewBox="0 0 20 20" aria-hidden="true"><circle cx="10" cy="10" r="10" fill="#d95d39"/><path d="M6.5 5.5l2 0 .8 2.2-1.2 .9a6 6 0 0 0 3.3 3.3l.9-1.2 2.2.8v2a1 1 0 0 1-1 1A8 8 0 0 1 5.5 6.5a1 1 0 0 1 1-1z" fill="#fff"/></svg>
        +1 800 555-0142
      </li>
      <li>
        <svg class="contact-icon" viewBox="0 0 20 20" aria-hidden="true"><circle cx="10" cy="10" r="10" fill="#d95d39"/><rect x="6.5" y="5" width="7" height="3" fill="#fff"/><rect x="5" y="8.5" width="10" height="5" rx="1" fill="#fff"/><rect x="7" y="12" width="6" height="3" fill="#fff" stroke="#d95d39" stroke-width=".6"/></svg>
        +1 702 555-0187
      </li>
      <li>
        <svg class="contact-icon" viewBox="0 0 20 20" aria-hidden="true"><circle cx="10" cy="10" r="10" fill="#d95d39"/><rect x="5" y="6.5" width="10" height="7" fill="#fff"/><path d="M5 6.5l5 4 5-4" fill="none" stroke="#d95d39" stroke-width="1"/></svg>
        graham@pelkusa.com
      </li>
      <li>
        <svg class="contact-icon" viewBox="0 0 20 20" aria-hidden="true"><circle cx="10" cy="10" r="10" fill="#d95d39"/><circle cx="10" cy="10" r="5" fill="none" stroke="#fff" stroke-width="1.2"/><ellipse cx="10" cy="10" rx="2" ry="5" fill="none" stroke="#fff" stroke-width="1"/><path d="M5 10h10" stroke="#fff" stroke-width="1"/></svg>
        www.pelkusa.com
      </li>
    </ul>
  </div>
  <span class="panel-notch" aria-hidden="true"></span>
</section>

</body>
</html>
```